Skin Care business card for esthetician that is home based

I need a business card for my esthetician business. I would like to use a picture provided.
I want the picture #1 that I have provided to be as the main background with my title and the moto underneath in smaller lettering. Below that as a seperate thing I would like my full name and underneath in small letters to say "esthetician".
As a seperate paragraph I would like my address then phone number, email and my website that I have provided in the business card details.
On the back side I would like my second picture to be small and in the top left corner and then have the "nice to haves" details to be at the center bottom of the card.
Target Market(s)
mosty women between 18 and 60 years old
Industry/Entity Type
Skin Care
Contact Information for Business Card
Coastline Skin Care - Main Title
Bringing out your natural glow! - motto
Lorena Bistrica Vondel -
Phone: 312.485.1937
7183 SW 9th Avenue
Dallow WA 98321
marlowskincare@examplemail.com
www.marlowskincare.example
Font styles to use
Requirements
Must have
- Picure I provided or other similar photo.
Nice to have
- On the back side:
Bringing out your natural glow!
www.marlowskincare.example

```html
<!DOCTYPE html>
<html lang="en">
<head>
<meta charset="utf-8">
<title>Coastline Skin Care – Business Card</title>
<link href="https://fonts.googleapis.com/css2?family=Playfair+Display:wght@400&family=Montserrat:wght@400;500&display=swap" rel="stylesheet">
<style>
  :root {
    --bg: #d9d4cf;
    --card-white: #ffffff;
    --ink: #1c1b1a;
    --accent: #c4692a;
    --photo-dark: #4a3a33;
    --photo-mid: #7a645a;
    --photo-light: #a89285;
    --portrait-light: #cfc8bd;
    --portrait-mid: #9d8d7c;
  }
  * { box-sizing: border-box; margin: 0; padding: 0; }
  html, body { width: 1200px; height: 716px; overflow: hidden; }
  body {
    background: var(--bg);
    font-family: "Montserrat", sans-serif;
    position: relative;
  }
  .card {
    position: absolute;
    top: 203px;
    width: 540px;
    height: 310px;
    overflow: hidden;
    box-shadow: 0 6px 18px rgba(0,0,0,0.25);
  }
  /* Front: photo background */
  .card--front { left: 30px; }
  .front-photo {
    position: absolute; inset: 0;
    background: radial-gradient(ellipse at 35% 30%, var(--photo-light) 0%, var(--photo-mid) 45%, var(--photo-dark) 100%);
  }
  .front-shade { position: absolute; inset: 0; background: rgba(40,28,24,0.35); }
  .front-brand {
    position: absolute; left: 180px; top: 74px; width: 330px;
    color: #fff;
  }
  .brand-name {
    font-family: "Playfair Display", serif;
    font-weight: 400; line-height: 1.1;
    white-space: nowrap;
  }
  .front-brand .brand-name { font-size: 34px; }
  .front-brand .motto {
    font-family: "Montserrat", sans-serif;
    font-size: 13px; margin-top: 12px; padding-left: 30px;
  }
  .front-web {
    position: absolute; left: 120px; top: 205px;
    color: #fff; font-size: 13px; letter-spacing: 0.3px;
  }
  /* Back: portrait + details */
  .card--back { left: 630px; background: var(--card-white); }
  .portrait {
    position: absolute; left: 0; top: 0; bottom: 0; width: 205px;
    background: linear-gradient(160deg, var(--portrait-light) 0%, var(--portrait-mid) 100%);
  }
  .details { position: absolute; left: 228px; top: 32px; right: 18px; color: var(--ink); }
  .details .brand-name { font-size: 29px; }
  .details .motto { font-size: 11px; margin-top: 8px; padding-left: 30px; }
  .details .name {
    font-family: "Playfair Display", serif;
    color: var(--accent); font-size: 18px; margin-top: 16px;
  }
  .details .address { font-size: 12.5px; line-height: 1.35; margin-top: 14px; }
  .contact { list-style: none; margin-top: 12px; font-size: 12px; line-height: 1.5; }
  .contact li { display: flex; align-items: center; gap: 7px; white-space: nowrap; }
  .contact svg { width: 11px; height: 11px; flex: none; fill: var(--accent); }
</style>
</head>
<body>
  <section class="card card--front">
    <div class="front-photo" role="img" aria-label="Spa photo of a woman receiving a facial mask with massage stones and a candle"></div>
    <div class="front-shade"></div>
    <div class="front-brand">
      <h1 class="brand-name">Coastline Skin Care</h1>
      <p class="motto">Bringing out your natural glow!</p>
    </div>
    <p class="front-web">www.marlowskincare.example</p>
  </section>

  <section class="card card--back">
    <div class="portrait" role="img" aria-label="Portrait of the esthetician in a white uniform"></div>
    <div class="details">
      <h2 class="brand-name">Coastline Skin Care</h2>
      <p class="motto">Bringing out your natural glow!</p>
      <p class="name">Lorena Bistrica Vondel</p>
      <p class="address">7183 SW 9th Avenue<br>Dallow WA 98321</p>
      <ul class="contact">
        <li><svg viewBox="0 0 24 24"><path d="M6.6 10.8a15 15 0 0 0 6.6 6.6l2.2-2.2c.3-.3.7-.4 1-.2 1.1.4 2.3.6 3.6.6.6 0 1 .4 1 1V20c0 .6-.4 1-1 1A17 17 0 0 1 3 4c0-.6.4-1 1-1h3.5c.6 0 1 .4 1 1 0 1.3.2 2.5.6 3.6.1.3 0 .7-.2 1z"/></svg>312.485.1937</li>
        <li><svg viewBox="0 0 24 24"><path d="M2 5h20v14H2z M2 5l10 8 10-8" stroke="#fff" stroke-width="1.5"/></svg>marlowskincare@examplemail.com</li>
        <li><svg viewBox="0 0 24 24"><circle cx="12" cy="12" r="10"/><path d="M2 12h20M12 2c3 3 3 17 0 20M12 2c-3 3-3 17 0 20" stroke="#fff" stroke-width="1.3" fill="none"/></svg>www.marlowskincare.example</li>
      </ul>
    </div>
  </section>
</body>
</html>
```